Web Design Project

*** This project has been temporarily placed on hold as the Logo Design needs to be completed first. You are all welcome to participate on it as well: http://gigs.pitchboardly.com/brief.aspx?id=482917 This project will be reopened soon***

Revamp current website adding newly designed logo and creating layout that is good on desktops, tablets, and cell phones.

Current website can be viewed at www.vennatistudio.com

Will you see the website is small but graphics heavy in the gallery. The gallery needs to be setup so that it is easy to maintain the links and update the photos.

Needs to have high visual impact.

I need a new logo and website layout designed for my partner's business. This is a birthday present. His business is interior painting, wallpapering and design. He also has access to a wide variety of products including carpet, fabrics, furniture, wallpaper, tile, countertops, etc. I have attached some screen shots of his website for reference. He is a one man shop and has a stellar reputation with his customers. He is on-time, very tidy, excellent with animals, and always finishes on time and on budget. There are no restrictions on colors or fonts. The logo needs to work well with the website, business cards and printed materials. The website needs to flow content for device size so it looks just as good on a cell phone or tablet as it does on a desktop computer. Whatever the heck that's called! Thanks. I am looking forward to seeing everyone's ideas.
Updates

Hi Designers, We've reopened this project as our logo design project has just completed. Please refer to the uploaded files and make use of either Horizontal or Vertical versions of the logo depending on what you think is suitable for your design proposals. We look forward to your creative submissions!

Target Market(s)

Consumers looking for interior design, painting, and wallpapering as well as interior products such as flooring, window treatments, reupholstering, counter tops, etc.

Industry/Entity Type

Cell Phone

Requirements
Must have
• Clean, sharp, visual impact (at least on the home page)
Should not have
• Clutter.

```html
<!DOCTYPE html>
<html lang="en">
<head>
<meta charset="utf-8">
<title>Vennati Interior Designs</title>
<link href="https://fonts.googleapis.com/css2?family=Open+Sans:ital,wght@0,400;0,600;0,700;1,400&family=Crimson+Text:ital,wght@0,400;0,600;1,400&display=swap" rel="stylesheet">
<style>
:root{
  --navy:#2b2448;
  --navy-deep:#261f40;
  --orange:#f7941d;
  --red:#c0392b;
  --ink:#333;
  --muted:#666;
  --band:#f5f5f7;
  --line:#e3e3e3;
  --footer-line:#4a4268;
  --white:#fff;
}
*{margin:0;padding:0;box-sizing:border-box}
html,body{width:1200px;height:2597px;overflow:hidden;background:var(--white)}
body{position:relative;font-family:"Open Sans",sans-serif;color:var(--ink)}
.abs{position:absolute}

/* hero */
.hero{left:0;top:0;width:1200px;height:748px;background:linear-gradient(180deg,#8a8f96 0%,#c9a983 28%,#6a5a4c 55%,#3a2f27 100%)}
.brand{left:161px;top:0;width:332px;height:120px;background:var(--white);display:flex;align-items:center;gap:14px;padding-left:20px}
.brand-mark{width:40px;height:40px;background:var(--navy);flex:none}
.brand-name{font-family:"Crimson Text",serif;font-weight:600;font-size:26px;color:var(--navy);letter-spacing:1px;line-height:1.05}
.nav{left:558px;top:31px;width:506px;height:62px;background:var(--navy);display:flex}
.nav a{color:var(--white);text-decoration:none;font-size:20px;display:flex;align-items:center;justify-content:center;white-space:nowrap;flex:1 1 auto;padding:0 10px}
.nav a.active{background:var(--orange);flex:0 0 117px}
.hero-title{left:0;top:386px;width:1200px;text-align:center;color:var(--white);font-size:44px;line-height:44px;font-weight:700}
.hero-sub{left:0;top:430px;width:1200px;text-align:center;color:var(--white);font-size:22px;line-height:26px}
.hero-btn{left:519px;top:553px;width:151px;height:49px;background:var(--orange);color:var(--white);font-size:17px;font-weight:700;display:flex;align-items:center;justify-content:center;border-radius:3px}
.arrow{top:400px;width:47px;height:47px}

/* welcome */
.welcome{left:0;top:790px;width:1200px;text-align:center}
.welcome h1{font-weight:400;font-size:55px;color:var(--navy);line-height:66px}
.welcome h1 .accent{color:var(--orange)}
.lede{font-size:14px;color:var(--muted);line-height:22px}
.welcome .lede{margin-top:18px}
.devices{left:182px;top:1060px;width:247px;height:252px;background:linear-gradient(135deg,#3a2b4a,#7a5b6c 50%,#2a2a30);border-radius:14px}
.intro{left:490px;top:1040px;width:572px}
.intro h2{font-size:29px;line-height:36px;font-weight:600;color:#111;margin-bottom:20px}
.intro .quote{font-family:"Crimson Text",serif;font-style:italic;font-size:18px;line-height:20px;color:#333;margin-bottom:12px}
.intro p{font-size:13.5px;line-height:19px;color:var(--muted)}
.intro .more{color:var(--red);font-size:15px;margin-top:22px}
.rule{left:0;top:1379px;width:1200px;height:2px;background:var(--line)}

/* services */
.services-head{left:0;top:1418px;width:1200px;text-align:center}
.services-head h2{font-weight:400;font-size:55px;line-height:70px;color:var(--navy)}
.services-head .lede{margin-top:2px}
.service{top:1571px;width:300px;text-align:center}
.service .icon{width:135px;height:135px;border-radius:50%;background:var(--orange);margin:0 auto;display:flex;align-items:center;justify-content:center}
.service h3{font-weight:400;font-size:20px;line-height:28px;color:#222;margin-top:18px}
.service p{font-family:"Crimson Text",serif;font-size:14px;line-height:16px;color:#444;width:220px;margin:8px auto 0}

/* testimonials & news */
.band{left:0;top:1875px;width:1200px;height:405px;background:var(--band)}
.section-title{font-size:32px;line-height:44px;color:var(--navy);font-weight:400;padding-bottom:10px;border-bottom:2px solid var(--line);white-space:nowrap}
.testimonials{left:182px;top:1918px;width:384px}
.testimonial-text{font-family:"Crimson Text",serif;font-size:15px;line-height:17px;color:#444;margin:22px 0 0 36px;position:relative;text-align:justify}
.testimonial-text::before{content:"\201C";position:absolute;left:-36px;top:-6px;color:#8a8fc0;font-size:34px;line-height:34px}
.avatar{left:213px;top:2137px;width:104px;height:104px;border-radius:50%;background:linear-gradient(135deg,#d9c3a8,#8a6b55);border:4px solid var(--white)}
.author{left:330px;top:2160px}
.author .name{font-family:"Crimson Text",serif;font-size:22px;line-height:26px;color:var(--red)}
.author .role{font-size:13px;line-height:20px;color:#444}
.news{left:714px;top:1918px;width:314px}
.news-item{display:flex;gap:18px;padding:16px 0 12px;border-bottom:2px solid var(--line)}
.news-date{width:66px;text-align:center;flex:none}
.news-date .day{font-family:"Crimson Text",serif;font-size:70px;line-height:64px;color:#111}
.news-date .mon{font-size:17px;line-height:22px;color:#222}
.news-body h4{font-family:"Crimson Text",serif;font-weight:400;font-size:24px;color:var(--red);line-height:26px}
.news-body p{font-family:"Crimson Text",serif;font-size:14px;line-height:16px;color:#333}
.news-body .see{font-size:14px;line-height:20px;color:var(--red);font-weight:600}

/* footer */
.footer{left:0;top:2280px;width:1200px;height:286px;background:var(--navy-deep)}
.fcol{top:2298px;width:160px;color:var(--white)}
.fcol h5{font-weight:400;font-size:26px;line-height:36px;margin-bottom:12px}
.fcol li{list-style:none;font-size:13px;height:39.5px;line-height:39.5px;border-bottom:1px solid var(--footer-line);white-space:nowrap}
.copyright{left:182px;top:2569px;font-size:14px;line-height:22px;color:#222}
</style>
</head>
<body>
<header>
  <div class="abs hero" role="img" aria-label="Photo of a rooftop terrace with a large parasol and lounge seating at sunset"></div>
  <div class="abs brand"><span class="brand-mark"></span><span class="brand-name">VENNATI<br>INTERIOR DESIGNS</span></div>
  <nav class="abs nav"><a class="active">HOME</a><a>ABOUT US</a><a>SERVICES</a><a>CONTACT</a></nav>
  <div class="abs hero-title">Clean, flat &amp; polished design</div>
  <div class="abs hero-sub">Proin facilisis tempor augue quis varius</div>
  <div class="abs hero-btn">SHOW MORE</div>
  <svg class="abs arrow" style="left:31px" viewBox="0 0 48 48"><circle cx="24" cy="24" r="22" fill="none" stroke="#fff" stroke-width="2.5"/><path d="M27 15 L18 24 L27 33" fill="none" stroke="#fff" stroke-width="3"/></svg>
  <svg class="abs arrow" style="left:1122px" viewBox="0 0 48 48"><circle cx="24" cy="24" r="22" fill="none" stroke="#fff" stroke-width="2.5"/><path d="M21 15 L30 24 L21 33" fill="none" stroke="#fff" stroke-width="3"/></svg>
</header>

<section>
  <div class="abs welcome">
    <h1>WELCOME TO<br><span class="accent">VENNATI</span> INTERIOR DESIGNS!</h1>
    <p class="lede">Search for anything people, topics, hashtags, your favorite sites and then flip through articles,<br>updates, photos and videos all in a beautiful magazine-style format.</p>
  </div>
  <div class="abs devices" role="img" aria-label="Tablet and phone showing the website"></div>
  <div class="abs intro">
    <h2>Good solutionss for your business!</h2>
    <p class="quote">With the various materials, colors, and finishes available the choices today can be daunting. By listening to you, I am able to pick just the right color, the right fabric, or the right furniture for your projects.</p>
    <p>Whether you are starting with a small project or a large project, I am ready to bring your ideas to life. It doesn't take a big budget to achieve dramatic effects. A wonderful new look is within anyone's reach. My guidance with the selection of colors, fabric, paint, wallpaper, and furniture, as well as the placement of items in a room, will help you achieve the results you desire – a beautiful home that is a joy to walk into and to show off!</p>
    <p class="more">READ MORE &gt;</p>
  </div>
  <div class="abs rule"></div>
</section>

<section>
  <div class="abs services-head">
    <h2>OUR SERVICES</h2>
    <p class="lede">Search for anything people, topics, hashtags, your favorite sites and then flip through articles</p>
  </div>
  <div class="abs service" style="left:138px">
    <div class="icon"><svg width="68" height="58" viewBox="0 0 70 60" fill="none" stroke="#fff" stroke-width="4"><rect x="4" y="4" width="62" height="52" rx="4"/><line x1="4" y1="30" x2="66" y2="30"/><line x1="27" y1="17" x2="43" y2="17"/><line x1="27" y1="43" x2="43" y2="43"/></svg></div>
    <h3>Amazing Service</h3>
    <p>Lorem ipsum dolor sit amet, consec tetuer adipiscing elit, sed diam non nummy nibh euismod tincidunt ut laoreet dolore magna.</p>
  </div>
  <div class="abs service" style="left:458px">
    <div class="icon"><svg width="68" height="68" viewBox="0 0 70 70" fill="#fff"><path d="M62 4 L66 8 L34 44 L26 36 Z"/><path d="M22 40 L30 48 C28 60 16 64 4 64 C10 58 8 44 22 40 Z"/></svg></div>
    <h3>Quality &amp; Design</h3>
    <p>Lorem ipsum dolor sit amet, consec tetuer adipiscing elit, sed diam non nummy nibh euismod tincidunt ut laoreet dolore magna.</p>
  </div>
  <div class="abs service" style="left:777px">
    <div class="icon"><svg width="70" height="62" viewBox="0 0 72 64" fill="none" stroke="#fff" stroke-width="4" stroke-linejoin="round"><path d="M4 10 L24 4 L48 10 L68 4 L68 54 L48 60 L24 54 L4 60 Z"/><line x1="24" y1="4" x2="24" y2="54"/><line x1="48" y1="10" x2="48" y2="60"/></svg></div>
    <h3>Smooth Drive</h3>
    <p>Lorem ipsum dolor sit amet, consec tetuer adipiscing elit, sed diam non nummy nibh euismod tincidunt ut laoreet dolore magna.</p>
  </div>
</section>

<section>
  <div class="abs band"></div>
  <div class="abs testimonials">
    <h2 class="section-title">CLIENT TESTIMONIALS</h2>
    <p class="testimonial-text">Lorem ipsum dolor sit amet, consectetuer adipiscing elit, sed diam nonummy nibh euismod tincidunt ut laoreet dolore magna aliquam erat volutpat. Ut wisi enim ad minim veniam, quis nostrud exerci tation ullamcorper suscipit lobortis nisl ut aliquip ex ea commodo consequat.</p>
  </div>
  <div class="abs avatar" role="img" aria-label="Portrait photo of the client"></div>
  <div class="abs author"><div class="name">Nora Callan</div><div class="role">CEO of Bright Path Company</div></div>
  <div class="abs news">
    <h2 class="section-title">LATEST NEWS</h2>
    <div class="news-item">
      <div class="news-date"><div class="day">15</div><div class="mon">FEB</div></div>
      <div class="news-body"><h4>Marketing Growth!</h4><p>Explore recommended reading in the Content Guide, including major publications.</p><div class="see">See More &gt;&gt;</div></div>
    </div>
    <div class="news-item">
      <div class="news-date"><div class="day">10</div><div class="mon">FEB</div></div>
      <div class="news-body"><h4>Marketing Growth!</h4><p>Explore recommended reading in the Content Guide, including major publications.</p><div class="see">See More &gt;&gt;</div></div>
    </div>
  </div>
</section>

<footer>
  <div class="abs footer"></div>
  <div class="abs fcol" style="left:184px"><h5>ABOUT</h5><ul><li>About HomeLine</li><li>Terms &amp; Conditions</li><li>Privacy Policy</li><li>Track Your Order</li><li>Disclaimer</li></ul></div>
  <div class="abs fcol" style="left:397px"><h5>NEW CARS</h5><ul><li>New Collection</li><li>Panther (2015)</li><li>Limo Collection</li><li>Exclusive Offers</li><li>Sale</li></ul></div>
  <div class="abs fcol" style="left:634px"><h5>FOLLOW US</h5><ul><li>Friendly</li><li>Chirper</li><li>Snapfolio</li><li>Reelhouse</li><li>Pinboardy</li></ul></div>
  <div class="abs fcol" style="left:875px"><h5>GENERAL</h5><ul><li>Webstore</li><li>FAQ</li><li>Size Guide</li><li>Delivery &amp; Returns</li></ul></div>
  <div class="abs copyright">© <b>HOMELINE</b> 2012-2015 ALL RIGHTS RESERVED</div>
</footer>
</body>
</html>
```